Marco Vessi Landing page

I need a Landing page for a website Marco Vessi. This is for an upscale clothing store for Men and Womens clothing and other items. It has to be elegant and unique in design and style.

Target Market(s)

Men, Women, Young adults 18-60

Coding

Number of Pages Required

1 page

Font styles to use
Decorative

Colors

Designer to choose colors to be used in the design.

```html
<!DOCTYPE html>
<html lang="en">
<head>
<meta charset="utf-8">
<title>Marco Vessi — Landing Page</title>
<link href="https://fonts.googleapis.com/css2?family=Cinzel:wght@400;500&family=Montserrat:wght@400;600;700;900&display=swap" rel="stylesheet">
<style>
:root{
  --black:#000000;
  --ink:#0d0d0d;
  --panel:#141414;
  --gold:#b8720c;
  --gold-deep:#9a5f08;
  --gold-light:#d79a2a;
  --gold-text:#c8923a;
  --white:#ffffff;
  --muted:#e9d6b8;
  --ghost-dark:rgba(255,255,255,0.07);
  --ghost-gold:rgba(0,0,0,0.09);
}
*{box-sizing:border-box;margin:0;padding:0}
html,body{width:1200px;height:3482px;overflow:hidden;background:var(--black)}
body{position:relative;font-family:"Montserrat",Arial,sans-serif;color:var(--white)}
.abs{position:absolute}
.serif{font-family:"Cinzel",Georgia,serif;font-weight:400}

/* header */
.header{left:0;top:0;width:1200px;height:128px;background:var(--black)}
.search{left:145px;top:47px;width:289px;height:37px;display:flex}
.search-input{flex:1;border:1px solid #555;background:var(--black);color:#ddd;font-size:11px;padding:0 14px;display:flex;align-items:center}
.search-btn{width:40px;background:var(--gold);display:flex;align-items:center;justify-content:center}
.brand{left:400px;top:44px;width:400px;text-align:center;font-size:28px;color:var(--gold-text);letter-spacing:1px}
.user-icon{left:976px;top:60px}
.cart-icon{left:1020px;top:56px}
.cart-count{left:1036px;top:44px;width:18px;height:18px;border-radius:50%;background:var(--gold);font-size:11px;color:var(--black);text-align:center;line-height:18px}

/* nav */
.nav{left:0;top:128px;width:1200px;height:48px;background:linear-gradient(180deg,var(--gold-light),var(--gold-deep));display:flex;justify-content:center;align-items:stretch}
.nav a{color:var(--white);text-decoration:none;font-size:15px;display:flex;align-items:center;padding:0 23px}
.nav a.active{background:rgba(0,0,0,0.18)}

/* hero */
.about-bg{left:0;top:740px;width:1200px;height:1400px;background:var(--panel)}
.hero-frame{left:0;top:176px;width:1200px;height:749px;background:var(--gold);clip-path:polygon(0 0,100% 0,100% 576px,50% 749px,0 576px)}
.hero-photo{left:0;top:176px;width:1200px;height:743px;background:radial-gradient(ellipse at 45% 45%,#3a2c26 0%,#1a1512 45%,#060606 100%);clip-path:polygon(0 0,100% 0,100% 570px,50% 743px,0 570px)}
.ghost{font-family:"Montserrat",Arial,sans-serif;font-weight:900;line-height:1;white-space:nowrap}
.ghost-home{left:-48px;top:442px;font-size:120px;color:var(--ghost-dark);transform:rotate(-90deg);transform-origin:center}
.hero-copy{left:650px;top:290px;width:506px;text-align:center}
.hero-title{font-size:54px;color:var(--gold-text);line-height:1.1}
.hero-sub{margin-top:22px;font-size:17px;line-height:23px}
.btn{display:inline-flex;align-items:center;gap:8px;border-radius:26px;font-weight:700;font-size:16px;color:var(--white);justify-content:center}
.btn-gold{background:var(--gold)}
.btn-black{background:var(--black)}
.hero-btn{left:812px;top:443px;width:183px;height:52px}
.dots{left:862px;top:540px;display:flex;gap:9px}
.dots span{width:9px;height:9px;border-radius:50%;background:var(--white)}
.dots span.on{background:transparent;border:2px solid var(--gold)}

/* about */
.ghost-about{left:960px;top:958px;font-size:120px;color:var(--ghost-dark);transform:rotate(-90deg);transform-origin:center}
.rule-title{display:flex;align-items:center;justify-content:center;gap:18px;width:1200px;left:0}
.rule-title i{display:block;width:90px;height:2px;background:currentColor;position:relative}
.rule-title i::after{content:"";position:absolute;top:-5px;width:8px;height:8px;border:2px solid currentColor;transform:rotate(45deg)}
.rule-title i.l::after{left:-6px}
.rule-title i.r::after{right:-6px}
.welcome-title{top:988px;font-size:40px;color:var(--gold-text)}
.welcome-text{left:210px;top:1055px;width:780px;text-align:center;font-size:14px;line-height:28px;color:#e8e8e8}
.about-btn{left:508px;top:1230px;width:183px;height:51px}

/* save */
.save-panel{left:0;top:1230px;width:600px;height:865px;background:var(--gold);clip-path:polygon(0 0,100% 202px,100% 615px,0 100%)}
.save-photo{left:600px;top:1230px;width:600px;height:865px;background:linear-gradient(135deg,#6e6e6e 0%,#4b3a2d 45%,#7a4a24 70%,#2c3d55 100%);clip-path:polygon(0 202px,100% 0,100% 100%,0 615px)}
.ghost-save{left:41px;top:1346px;font-size:100px;color:var(--ghost-gold)}
.save-title{left:36px;top:1508px;display:flex;align-items:center;gap:20px;font-size:40px;color:var(--white)}
.save-title i{display:block;width:72px;height:2px;background:var(--white);position:relative}
.save-title i::after{content:"";position:absolute;top:-5px;width:8px;height:8px;border:2px solid var(--white);transform:rotate(45deg)}
.save-title i.l::after{left:-6px}
.save-title i.r::after{right:-6px}
.save-lead{left:145px;top:1582px;width:420px;font-size:18px;font-weight:700;line-height:28px}
.save-note{left:145px;top:1672px;width:400px;font-size:13px;line-height:28px;color:#fbe9cc}
.save-btn{left:145px;top:1757px;width:182px;height:51px}

/* products */
.featured-title{top:2030px;font-size:40px;color:var(--gold-text)}
.ghost-products{left:262px;top:2496px;font-size:118px;color:var(--ghost-dark)}
.diamond{width:var(--s);height:var(--s);border-radius:28px;transform:translate(-50%,-50%) rotate(45deg);overflow:hidden}
.d-left{left:295px;top:2307px;--s:213px;background:linear-gradient(135deg,#e6e3df,#b9b3ad)}
.d-right{left:905px;top:2307px;--s:211px;background:linear-gradient(135deg,#d7d7d5,#a9a9a7)}
.d-mid{left:600px;top:2306px;--s:270px;background:linear-gradient(135deg,#9ca1a4,#2c4d7a 60%,#1f2f44)}
.arrows{left:566px;top:2520px;display:flex;gap:7px}
.arrows span{width:31px;height:31px;border-radius:50%;background:var(--gold);display:flex;align-items:center;justify-content:center}

/* blog */
.blog{left:0;top:2615px;width:1200px;height:567px;background:var(--gold)}
.ghost-blog{left:878px;top:3068px;font-size:110px;color:var(--ghost-gold)}
.blog-title{top:2690px;font-size:40px;color:var(--white)}
.card{top:2777px;width:285px}
.card-img{height:178px}
.card-date{position:absolute;left:12px;top:163px;width:108px;height:32px;background:var(--black);font-size:12px;font-weight:600;display:flex;align-items:center;justify-content:center}
.card h3{margin-top:40px;font-size:13px;font-weight:700}
.card p{margin-top:12px;font-size:12px;line-height:21px;color:#fbe9cc}
.card a{display:block;margin-top:14px;font-size:11px;font-weight:700;color:var(--white);text-decoration:underline}

/* footer */
.footer{left:0;top:3182px;width:1200px;height:237px;background:var(--black)}
.foot-h{font-size:20px;color:var(--white)}
.sub-h{left:145px;top:3234px}
.sub-p{left:145px;top:3272px;font-size:13px}
.sub-form{left:145px;top:3320px;display:flex;height:40px}
.sub-input{width:223px;background:var(--white);color:#555;font-size:11px;display:flex;align-items:center;padding-left:12px}
.sub-btn{width:91px;background:var(--gold);font-size:14px;font-weight:700;display:flex;align-items:center;justify-content:center}
.foot-brand{left:473px;top:3290px;width:400px;text-align:center;font-size:34px;color:var(--gold-text)}
.hours-h{left:886px;top:3234px}
.hours{left:886px;top:3272px;font-size:13px;line-height:22px}
.social{left:888px;top:3355px;display:flex;gap:18px}
.social span{width:20px;height:20px;border-radius:50%;background:var(--white)}
.copyright{left:0;top:3419px;width:1200px;height:63px;background:var(--black);font-size:13px;display:flex;align-items:center;justify-content:center;gap:8px}
</style>
</head>
<body>

<!-- header -->
<header class="abs header">
  <div class="abs search">
    <div class="search-input">Search..</div>
    <div class="search-btn">
      <svg width="14" height="14" viewBox="0 0 14 14"><circle cx="6" cy="6" r="4.5" fill="none" stroke="#fff" stroke-width="2"/><line x1="9.3" y1="9.3" x2="13" y2="13" stroke="#fff" stroke-width="2"/></svg>
    </div>
  </div>
  <div class="abs brand serif">Marco Vessi</div>
  <svg class="abs user-icon" width="30" height="30" viewBox="0 0 30 30"><circle cx="15" cy="15" r="13" fill="none" stroke="#ccc" stroke-width="1.6"/><circle cx="15" cy="12" r="4.5" fill="none" stroke="#ccc" stroke-width="1.6"/><path d="M7 24c2-5 14-5 16 0" fill="none" stroke="#ccc" stroke-width="1.6"/></svg>
  <svg class="abs cart-icon" width="30" height="32" viewBox="0 0 30 32"><path d="M9 12a6 6 0 0 1 12 0" fill="none" stroke="#ccc" stroke-width="1.8"/><rect x="3" y="12" width="24" height="4" fill="none" stroke="#ccc" stroke-width="1.8"/><path d="M5 16l2 13h16l2-13" fill="none" stroke="#ccc" stroke-width="1.8"/><line x1="11" y1="19" x2="11" y2="26" stroke="#ccc" stroke-width="1.6"/><line x1="15" y1="19" x2="15" y2="26" stroke="#ccc" stroke-width="1.6"/><line x1="19" y1="19" x2="19" y2="26" stroke="#ccc" stroke-width="1.6"/></svg>
  <div class="abs cart-count">0</div>
</header>

<nav class="abs nav">
  <a class="active" href="#">HOME</a>
  <a href="#">ABOUT US</a>
  <a href="#">SHOP</a>
  <a href="#">CATEGORIES</a>
  <a href="#">NEWS</a>
  <a href="#">CONTACT US</a>
</nav>

<!-- hero -->
<div class="abs about-bg" role="img" aria-label="Dark damask patterned background"></div>
<div class="abs hero-frame"></div>
<div class="abs hero-photo" role="img" aria-label="Fashion photo of an elegant couple on a leather sofa"></div>
<div class="abs ghost ghost-home">HOME</div>
<section class="abs hero-copy">
  <h1 class="hero-title serif">Marco Vessi</h1>
  <p class="hero-sub">Sed ut perspiciatis unde omnis iste natus<br>error sit voluptatem accusanti</p>
</section>
<a class="abs btn btn-gold hero-btn">GET STARTED
  <svg width="16" height="16" viewBox="0 0 16 16"><circle cx="8" cy="8" r="8" fill="#fff"/><path d="M6.5 4.5l3.5 3.5-3.5 3.5" fill="none" stroke="#b8720c" stroke-width="2"/></svg></a>
<div class="abs dots"><span></span><span></span><span class="on"></span><span></span><span></span></div>

<!-- about -->
<div class="abs ghost ghost-about">ABOUT</div>
<h2 class="abs rule-title welcome-title serif"><i class="l"></i>Welcome to Marco Vessi<i class="r"></i></h2>
<p class="abs welcome-text">Sed ut perspiciatis unde omnis iste natus error sit voluptatem accusantium doloremque laudantium, totam rem aperiam, eaque ipsa quae ab illo inventore veritatis et quasi architecto beatae vitae dicta sunt explicmo enim ipsam voluptatem quia voluptas sit aspernatur aut odit aut fugit, sed quia consequuntur magni dolores eos qui ratione voluptatem sequi nesciune porro quisquam est, qui dolorem ipsum quia dolor sit amet, consectetur adipisci veli sed quia non numquam eius modi tempora incidunt ut labore et dolore magnam aliquam quaerat voluptatem</p>
<a class="abs btn btn-gold about-btn">READ MORE
  <svg width="16" height="16" viewBox="0 0 16 16"><circle cx="8" cy="8" r="8" fill="#fff"/><path d="M6.5 4.5l3.5 3.5-3.5 3.5" fill="none" stroke="#b8720c" stroke-width="2"/></svg></a>

<!-- save -->
<div class="abs save-panel"></div>
<div class="abs save-photo" role="img" aria-label="Photo of a young couple in leather jackets on a bench"></div>
<div class="abs ghost ghost-save">SAVE</div>
<h2 class="abs save-title serif"><i class="l"></i>Save upto 50%<i class="r"></i></h2>
<p class="abs save-lead">Sed ut perspiciatis unde omnis iste natus error sit voluptatem accusantium doloremque laudantium totam rem aperiam</p>
<p class="abs save-note">nesciune porro quisquam est, qui dolorem ipsum quia dolor sit amet, consectetur adipisci veli..</p>
<a class="abs btn btn-black save-btn">READ MORE
  <svg width="16" height="16" viewBox="0 0 16 16"><circle cx="8" cy="8" r="8" fill="#fff"/><path d="M6.5 4.5l3.5 3.5-3.5 3.5" fill="none" stroke="#000" stroke-width="2"/></svg></a>

<!-- products -->
<h2 class="abs rule-title featured-title serif"><i class="l"></i>Featured Products<i class="r"></i></h2>
<div class="abs ghost ghost-products">PRODUCTS</div>
<div class="abs diamond d-left" role="img" aria-label="Product photo of a woman in a polka dot blouse with a handbag"></div>
<div class="abs diamond d-right" role="img" aria-label="Product photo of a woman in a white t-shirt"></div>
<div class="abs diamond d-mid" role="img" aria-label="Product photo of a man in a blue blazer and sunglasses"></div>
<div class="abs arrows">
  <span><svg width="10" height="12" viewBox="0 0 10 12"><path d="M7 1L2 6l5 5" fill="none" stroke="#fff" stroke-width="2"/></svg></span>
  <span><svg width="10" height="12" viewBox="0 0 10 12"><path d="M3 1l5 5-5 5" fill="none" stroke="#fff" stroke-width="2"/></svg></span>
</div>

<!-- blog -->
<section class="abs blog"></section>
<div class="abs ghost ghost-blog">BLOG</div>
<h2 class="abs rule-title blog-title serif"><i class="l"></i>Blog&nbsp; Posts<i class="r"></i></h2>

<article class="abs card" style="left:145px">
  <div class="card-img" role="img" aria-label="Flat lay of travel accessories, shoes and bags" style="background:linear-gradient(135deg,#f2f0ed,#c9b9a4)"></div>
  <div class="card-date">24 JUNE,2019</div>
  <h3>UM QUIA DOLOR SIT AMETONSECTE</h3>
  <p>Sed ut perspiciatis unde omnis iste natus<br>error sit voluptatem accusantium</p>
  <a href="#">READ MORE</a>
</article>
<article class="abs card" style="left:458px">
  <div class="card-img" role="img" aria-label="Photo of a couple in dark winter coats" style="background:linear-gradient(135deg,#3a3a3a,#121212)"></div>
  <div class="card-date">24 JUNE,2019</div>
  <h3>UM QUIA DOLOR SIT AMETONSECTE</h3>
  <p>Sed ut perspiciatis unde omnis iste natus<br>error sit voluptatem accusantium</p>
  <a href="#">READ MORE</a>
</article>
<article class="abs card" style="left:770px">
  <div class="card-img" role="img" aria-label="Photo of a couple in sunglasses in the city" style="background:linear-gradient(135deg,#d9d9d9,#6f6f6f)"></div>
  <div class="card-date">24 JUNE,2019</div>
  <h3>UM QUIA DOLOR SIT AMETONSECTE</h3>
  <p>Sed ut perspiciatis unde omnis iste natus<br>error sit voluptatem accusantium</p>
  <a href="#">READ MORE</a>
</article>

<!-- footer -->
<footer class="abs footer"></footer>
<h4 class="abs foot-h sub-h serif">SUBSCRIBE TO NEWSLETTER</h4>
<p class="abs sub-p">Lorem ipsum dolor sit amet,</p>
<div class="abs sub-form"><div class="sub-input">Enter Email</div><div class="sub-btn">SUBMIT</div></div>
<div class="abs foot-brand serif">Marco Vessi</div>
<h4 class="abs foot-h hours-h serif">OPENING HOURS</h4>
<p class="abs hours">Mon - Fri : 10 am to 6pm<br>Saturday : 9 am to 3pm<br>Sunday : closed</p>
<div class="abs social" aria-label="Social links"><span></span><span></span><span></span><span></span><span></span></div>
<div class="abs copyright"><span>© copyright 2019 Marco Vessi.All Rights Reserved</span><span>|</span><span>Privacy policy</span><span>|</span><span>Terms and use</span></div>

</body>
</html>
```